Retail Sign for Houseplant Campaign

Please make Portrait style not landscape Sign will measure 3 to 4 foot tall by 22.2inches and place on rolling racks of houseplants for a retail promotion in The Yard Locker. The theme of the promotion will be "Bring your home to life with Houseplants!" Selling points which should be on the sign are Houseplants * improve your mood * reduce fatigue * improve focus. Please put signage in landscape format and include yard locker and verdant makings logo.

Just recovered from covid. Im sorry for the delay

Target Market(s)

People who love plants

Industry/Entity Type

Retail

Colors
00AB8E
00BBA5
67D7C9
C6EFE9
E9F9F6
59FF00
82FF00
B8FF75
E3FFCB
F4FFEA
FFF300
FFF600
FEFA6F
FFFEC7
FFFEE8
FFC000
F8CF3A
FAE287
FDF2CF
FEFAEE

Requirements
Must have
• Must feel energetic and encourage people to buy plants. Should include 1-2 photos and the selling points listed

```html
<!DOCTYPE html>
<html lang="en">
<head>
<meta charset="utf-8">
<title>Bring Your Home to Life with Houseplants</title>
<link href="https://fonts.googleapis.com/css2?family=Bebas+Neue&family=Oswald:wght@500;600&family=Kaushan+Script&display=swap" rel="stylesheet">
<style>
  :root {
    --green-deep: #4f8a1c;
    --green-mid: #6fae23;
    --green-light: #8cc63f;
    --yellow-bright: #fff600;
    --yellow-warm: #ffc000;
    --yellow-sun: #f8cf3a;
    --peach: #fbe3c2;
    --peach-light: #fdf2cf;
    --text-white: #ffffff;
    --text-dark: #1f3b12;
    --tick-green: #5fa81e;
    --shadow: rgba(20, 40, 5, 0.55);
  }
  * { margin: 0; padding: 0; box-sizing: border-box; }
  html, body { width: 720px; height: 1200px; overflow: hidden; background: #ffffff; }
  .sign {
    position: relative;
    width: 720px;
    height: 1200px;
    overflow: hidden;
    background: var(--peach);
  }
  .lifestyle-photo {
    position: absolute;
    left: 0; top: 400px;
    width: 720px; height: 400px;
    background: linear-gradient(135deg, var(--yellow-sun) 0%, var(--yellow-warm) 55%, #f5a800 100%);
  }
  .backdrop { position: absolute; left: 0; top: 0; width: 720px; height: 1200px; }
  .headline {
    position: absolute;
    left: 0; top: 30px; width: 720px;
    text-align: center;
    color: var(--text-white);
  }
  .headline-top, .headline-bottom {
    font-family: "Bebas Neue", "Oswald", sans-serif;
    font-size: 112px;
    line-height: 0.95;
    letter-spacing: 2px;
    text-shadow: 3px 4px 0 var(--shadow);
  }
  .headline-home {
    font-family: "Bebas Neue", "Oswald", sans-serif;
    font-size: 250px;
    line-height: 0.82;
    letter-spacing: 4px;
    background: linear-gradient(180deg, #ffffff 0%, var(--yellow-bright) 45%, var(--yellow-warm) 100%);
    -webkit-background-clip: text;
    background-clip: text;
    color: transparent;
    filter: drop-shadow(5px 6px 0 var(--shadow));
  }
  .headline-script {
    font-family: "Kaushan Script", cursive;
    font-size: 66px;
    line-height: 1;
    margin-top: -6px;
    text-shadow: 3px 3px 0 var(--shadow);
  }
  .benefits {
    position: absolute;
    left: 118px; top: 810px;
    list-style: none;
  }
  .benefit {
    display: flex;
    align-items: center;
    gap: 22px;
    height: 58px;
    font-family: "Oswald", sans-serif;
    font-weight: 600;
    font-size: 42px;
    color: var(--text-dark);
    text-transform: uppercase;
    letter-spacing: 0.5px;
  }
  .tick { width: 40px; height: 40px; flex: none; }
  .foliage-photo {
    position: absolute;
    left: 0; top: 1040px;
    width: 720px; height: 160px;
    background: linear-gradient(180deg, rgba(110,170,60,0) 0%, #5d9a34 35%, #2f6a22 100%);
  }
</style>
</head>
<body>
<main class="sign">
  <div class="lifestyle-photo" role="img" aria-label="Photo of a smiling woman giving thumbs up, sitting cross-legged with a laptop on a white table beside potted houseplants, against a bright yellow wall"></div>

  <svg class="backdrop" viewBox="0 0 720 1200" aria-hidden="true">
    <defs>
      <linearGradient id="topGreen" x1="0" y1="0" x2="0" y2="1">
        <stop offset="0" stop-color="var(--green-deep)"/>
        <stop offset="1" stop-color="var(--green-light)"/>
      </linearGradient>
      <linearGradient id="lowerPeach" x1="0" y1="0" x2="0" y2="1">
        <stop offset="0" stop-color="var(--peach)"/>
        <stop offset="1" stop-color="var(--peach-light)"/>
      </linearGradient>
    </defs>
    <polygon points="0,0 720,0 720,490 0,610" fill="url(#topGreen)"/>
    <polygon points="0,780 720,745 720,1200 0,1200" fill="url(#lowerPeach)"/>
  </svg>

  <header class="headline">
    <div class="headline-top">Bring Your</div>
    <div class="headline-home">Home</div>
    <div class="headline-script">to life with</div>
    <div class="headline-bottom">Houseplants!</div>
  </header>

  <ul class="benefits">
    <li class="benefit">
      <svg class="tick" viewBox="0 0 40 40" aria-hidden="true"><circle cx="20" cy="20" r="18" fill="none" stroke="var(--tick-green)" stroke-width="3"/><path d="M11 20 L18 27 L30 13" fill="none" stroke="var(--tick-green)" stroke-width="4.5" stroke-linecap="round" stroke-linejoin="round"/></svg>
      Houseplants
    </li>
    <li class="benefit">
      <svg class="tick" viewBox="0 0 40 40" aria-hidden="true"><circle cx="20" cy="20" r="18" fill="none" stroke="var(--tick-green)" stroke-width="3"/><path d="M11 20 L18 27 L30 13" fill="none" stroke="var(--tick-green)" stroke-width="4.5" stroke-linecap="round" stroke-linejoin="round"/></svg>
      Improve your mood
    </li>
    <li class="benefit">
      <svg class="tick" viewBox="0 0 40 40" aria-hidden="true"><circle cx="20" cy="20" r="18" fill="none" stroke="var(--tick-green)" stroke-width="3"/><path d="M11 20 L18 27 L30 13" fill="none" stroke="var(--tick-green)" stroke-width="4.5" stroke-linecap="round" stroke-linejoin="round"/></svg>
      Reduce fatigue
    </li>
    <li class="benefit">
      <svg class="tick" viewBox="0 0 40 40" aria-hidden="true"><circle cx="20" cy="20" r="18" fill="none" stroke="var(--tick-green)" stroke-width="3"/><path d="M11 20 L18 27 L30 13" fill="none" stroke="var(--tick-green)" stroke-width="4.5" stroke-linecap="round" stroke-linejoin="round"/></svg>
      Improve focus
    </li>
  </ul>

  <div class="foliage-photo" role="img" aria-label="Photo of lush green houseplant leaves, snake plants and palms, rising along the bottom edge"></div>
</main>
</body>
</html>
```